HVAC company business card design

We need a business card design for a HVAC company. The design must look professional. Both sides will be used. The total data to be on the business card is
Name
Position
Email
Direct Phone/Moile Phone
Company Contacts /Address, Phone, Fax, web)
All data will be submit once the design is confirmed. For generic purposes use;
Cem Orkut
Managing Director
+902324418352 (Mobile)
4718 Sokak No: 9 KGTB Alsancak IZMIR TURKEY
Tel: +902324418352 Fax : +902324418359
www.ozkivra.com.tr

Target Market(s)

HVAC

Industry/Entity Type

Business

Contact Information for Business Card

The total data to be on the business card is
Name
Position
Email
Direct Phone/Moile Phone
Cem Orkut
Managing Director
+902324418352 (Mobile)
www.ozkivra.com.tr
The BC will use both sides of the card. The front will include the full logo and the details for the business card holder. The business card can be divided into vertical/horizontal or to a special shape. The common data like the company address/phone/fax should be indicated elsewehere. The back can contain some part or the whole logo and must contain the web address.

Font styles to use
Serif
Sans Serif

Colors
0355a3
cfdfed

Requirements
Should not have
• Please be careful with the fonts, it shouldnt be too small or too big and must not interfere with the logo fonts. If you need to use a curvy shape please do not use as the logo is already curvy or use the curves from the logo (if it looks good, otherwise forget it)
• We are not in favor of pictograms, only if they are perfect use them.

```html
<!DOCTYPE html>
<html lang="en">
<head>
<meta charset="utf-8">
<title>Ozkivra – Business Card</title>
<link href="https://fonts.googleapis.com/css2?family=Open+Sans:wght@400;600;700&display=swap" rel="stylesheet">
<style>
  :root{
    --stage:#d9d9d9;
    --navy:#3b4459;
    --navy-light:#5b6580;
    --brand-blue:#3a72c0;
    --text-blue:#3d6fb3;
    --band-light:#d3e0ee;
    --band-grey:#bccbda;
    --rule:#b9cde2;
    --paper-top:#e6e6e6;
    --paper:#ffffff;
    --address:#e3e8f0;
  }
  *{margin:0;padding:0;box-sizing:border-box}
  html,body{width:1200px;height:900px;overflow:hidden}
  body{background:var(--stage);font-family:"Open Sans",Arial,sans-serif;position:relative}
  .card{position:absolute;width:540px;height:330px;border-radius:16px;overflow:hidden;
        box-shadow:0 6px 18px rgba(0,0,0,.25)}
  .card-front{left:50px;top:100px;background:linear-gradient(170deg,var(--paper-top),var(--paper) 45%)}
  .card-back{left:610px;top:470px;background:linear-gradient(90deg,var(--navy-light),var(--navy))}

  .front-bands{position:absolute;inset:0}
  .brand{position:absolute;left:50px;top:52px;display:flex;align-items:center;gap:14px}
  .brand-dot{width:54px;height:54px;border-radius:50%;background:var(--brand-blue)}
  .brand-name{font-size:46px;font-weight:700;color:var(--navy);letter-spacing:1px}

  .holder{position:absolute;left:0;right:0;top:122px;text-align:center}
  .holder-name{font-size:24px;font-weight:700;color:var(--navy)}
  .holder-role{font-size:13px;color:var(--text-blue);margin-top:-2px}
  .rule{position:absolute;height:1px;background:var(--rule)}
  .rule-left{left:0;width:190px;top:180px}
  .rule-right{right:0;width:190px;top:150px}

  .contact{position:absolute;font-size:14px;color:var(--text-blue);line-height:26px}
  .contact-left{right:290px;top:210px;text-align:right}
  .contact-right{left:290px;top:198px}
  .contact-row{display:flex;align-items:center;gap:8px}
  .contact-left .contact-row{justify-content:flex-end}
  .icon{width:14px;height:14px;fill:var(--navy)}
  .address{position:absolute;left:0;right:0;bottom:18px;text-align:center;font-size:14px;color:var(--address)}

  .back-brand{position:absolute;left:0;right:0;top:120px;display:flex;justify-content:center;align-items:center;gap:12px}
  .back-dot{width:40px;height:40px;border-radius:50%;background:var(--brand-blue)}
  .back-name{font-size:34px;font-weight:700;color:var(--paper);letter-spacing:1px}
  .web{position:absolute;left:0;right:0;top:186px;text-align:center;font-size:13px;letter-spacing:4px;color:var(--brand-blue)}
</style>
</head>
<body>
  <section class="card card-front">
    <svg class="front-bands" width="540" height="330" viewBox="0 0 540 330">
      <rect x="0" y="205" width="270" height="125" fill="var(--band-light)"/>
      <rect x="270" y="195" width="270" height="67" fill="var(--band-grey)"/>
      <rect x="270" y="262" width="270" height="68" fill="var(--navy)"/>
      <rect x="0" y="275" width="270" height="55" fill="var(--navy)"/>
      <line x1="0" y1="205" x2="270" y2="205" stroke="var(--navy)" stroke-width="2"/>
      <polygon points="258,205 270,205 264,213" fill="var(--navy)"/>
    </svg>

    <div class="brand">
      <span class="brand-dot"></span>
      <span class="brand-name">OZKIVRA</span>
    </div>

    <div class="rule rule-right"></div>
    <div class="rule rule-left"></div>
    <div class="holder">
      <div class="holder-name">Cem Orkut</div>
      <div class="holder-role">Managing Director</div>
    </div>

    <div class="contact contact-left">
      <div class="contact-row">+902324418352
        <svg class="icon" viewBox="0 0 14 14"><rect x="3" y="0" width="8" height="14" rx="1.5"/><rect x="4.5" y="2" width="5" height="8" fill="var(--band-light)"/></svg>
      </div>
      <div class="contact-row">+902324418359
        <svg class="icon" viewBox="0 0 14 14"><path d="M1 4c0-2 3-3 6-3s6 1 6 3v1H10V4H4v1H1z"/><rect x="2" y="7" width="10" height="6" rx="1"/></svg>
      </div>
    </div>

    <div class="contact contact-right">
      <div class="contact-row">
        <svg class="icon" viewBox="0 0 14 14"><rect x="3" y="1" width="8" height="4"/><rect x="1" y="5" width="12" height="6" rx="1"/><rect x="3" y="9" width="8" height="4" fill="var(--band-grey)" stroke="var(--navy)"/></svg>
        +902324418352
      </div>
      <div class="contact-row">
        <svg class="icon" viewBox="0 0 14 14"><rect x="1" y="3" width="12" height="8"/><path d="M1 3l6 5 6-5" fill="none" stroke="var(--band-grey)" stroke-width="1.2"/></svg>
        cem_orkut@ozkivra.com.tr
      </div>
    </div>

    <div class="address">4718 Sokak No: 9 KGTB Alsancak IZMIR TURKEY</div>
  </section>

  <section class="card card-back">
    <div class="back-brand">
      <span class="back-dot"></span>
      <span class="back-name">OZKIVRA</span>
    </div>
    <div class="web">www.ozkivra.com.tr</div>
  </section>
</body>
</html>
```